Design Shopify E-Commerce Website for Men's Products

Design a Shopify website for men to sell our men's jewelry, cigar and bar accessories, and other men's products. Design should be hip, with like a rock n' roll, biker, whiskey driker flare. Name of the company is "Ironvale Locker" and website will be www.IronvaleLocker.com
Homepage will have navigation bar with three categories: Men's Jewelry, Cigar & Bar Products, Man Cave Swag
I will upload our logo, inspiration type pictures and some of the products that we sell
Theme colors should be mainly dark: black, grey, brown, gold

```html
<!DOCTYPE html>
<html lang="en">
<head>
<meta charset="utf-8">
<title>Ironvale Locker — Men's Products</title>
<link href="https://fonts.googleapis.com/css2?family=Playfair+Display:wght@400;500;700&display=swap" rel="stylesheet">
<style>
:root{
  --black:#000000;
  --white:#ffffff;
  --text:#e6e6e6;
  --gold:#c9a53f;
  --gold-soft:#b8963a;
  --serif:'Playfair Display', Georgia, serif;
}
*{margin:0;padding:0;box-sizing:border-box}
html,body{width:1200px;height:4389px;overflow:hidden;background:var(--black)}
body{position:relative;font-family:var(--serif);color:var(--white)}
.abs{position:absolute}
.hero{left:0;top:0;width:1200px;height:622px;
  background:
    radial-gradient(ellipse 260px 220px at 560px 360px,rgba(150,150,150,.55),rgba(150,150,150,0) 100%),
    radial-gradient(ellipse 200px 260px at 900px 300px,rgba(120,120,120,.5),rgba(120,120,120,0) 100%),
    radial-gradient(ellipse 180px 200px at 300px 470px,rgba(110,110,110,.45),rgba(110,110,110,0) 100%),
    radial-gradient(ellipse 160px 300px at 1120px 420px,rgba(100,100,100,.4),rgba(100,100,100,0) 100%),
    linear-gradient(90deg,#070707 0%,#1c1c1c 40%,#262626 70%,#141414 100%)}
.hero::after{content:"";position:absolute;left:0;right:0;bottom:0;height:90px;background:linear-gradient(180deg,rgba(0,0,0,0),#000)}
.nav a{position:absolute;top:56px;color:var(--white);font-size:17px;text-decoration:none}
.nav .small{font-size:14px;top:59px}
.nav .small svg{vertical-align:-1px;margin-left:4px}
.brand{left:500px;top:30px;width:200px;text-align:center;font-size:20px;color:var(--gold);font-weight:500;letter-spacing:1px}
.hero-kicker{left:99px;top:188px;font-size:35px;color:var(--gold);letter-spacing:1px}
.hero-title{left:99px;top:240px;font-size:52px;font-weight:700;line-height:62px;letter-spacing:1px}
.hero-lead{left:99px;top:371px;font-size:16px;color:var(--text)}
.btn{display:block;border:2px solid var(--gold-soft);color:var(--gold);font-size:21px;text-align:center;line-height:48px;text-decoration:none}
.scroll{left:1066px;top:476px;width:60px;height:180px}
.scroll span{position:absolute;left:10px;top:0;writing-mode:vertical-rl;transform:rotate(180deg);color:var(--gold);font-size:15px;height:120px;text-align:center}
.scroll i{position:absolute;left:36px;top:0;width:2px;height:180px;background:var(--white)}
.eyebrow{font-size:15px;color:var(--white);text-align:center;width:1200px;left:0}
.section-title{font-size:44px;width:1200px;left:0;text-align:center;font-weight:400}
.card{width:321px;height:447px;border:2px solid var(--gold-soft);top:861px}
.card .photo{position:absolute;left:17px;top:19px;width:284px;height:348px;border-radius:8px}
.card p{position:absolute;left:0;right:0;top:392px;text-align:center;font-size:20px}
.band{left:0;width:1200px}
.about{top:1449px;height:921px;background:linear-gradient(180deg,#000 0%,#262626 10%,#3a3a3a 45%,#333 80%,#000 100%)}
.rider{left:560px;top:1460px;width:640px;height:900px;
  background:
    radial-gradient(ellipse 150px 330px at 360px 470px,rgba(20,20,20,.85),rgba(20,20,20,0) 100%),
    radial-gradient(ellipse 340px 430px at 390px 400px,#e8e8e8 0%,#b4b4b4 45%,rgba(80,80,80,0) 100%);
  -webkit-mask-image:linear-gradient(90deg,transparent 0%,#000 30%),linear-gradient(180deg,transparent 0%,#000 12%,#000 85%,transparent 100%);
  -webkit-mask-composite:source-in;mask-composite:intersect;
  mask-image:linear-gradient(90deg,transparent 0%,#000 30%),linear-gradient(180deg,transparent 0%,#000 12%,#000 85%,transparent 100%)}
.kicker{font-size:15px;color:var(--white)}
.heading{font-size:44px;font-weight:400}
.copy{font-size:14.5px;line-height:25.8px;color:var(--text);white-space:nowrap}
.product{width:242px;height:181px;top:2644px;background:var(--white);border-radius:6px}
.product .thumb{position:absolute;left:56px;top:20px;width:130px;height:130px;border-radius:4px}
.pname{top:2845px;width:242px;text-align:center;font-size:17px;color:var(--text)}
.price{top:2875px;width:242px;text-align:center;font-size:20px;font-weight:700}
.charm{top:3052px;height:920px;background:linear-gradient(180deg,#000 0%,#17130f 10%,#211a14 50%,#17120e 88%,#000 100%)}
.glass{left:0;top:3140px;width:520px;height:760px;
  background:
    radial-gradient(ellipse 200px 130px at 210px 400px,#b5621f 0%,#7a3a12 50%,rgba(60,28,10,0) 100%),
    radial-gradient(ellipse 260px 330px at 220px 380px,rgba(90,55,30,.9) 0%,rgba(50,30,16,.7) 60%,rgba(30,20,12,0) 100%);
  -webkit-mask-image:radial-gradient(ellipse 60% 55% at 40% 52%,#000 60%,transparent 100%);
  mask-image:radial-gradient(ellipse 60% 55% at 40% 52%,#000 60%,transparent 100%)}
.footer-brand{left:94px;top:4058px;width:226px;height:213px;display:flex;align-items:center;justify-content:center;font-size:26px;color:var(--gold);font-weight:500;text-align:center}
.fhead{font-size:27px;color:var(--gold);font-weight:500;top:4058px}
.flinks{list-style:none;top:4113px}
.flinks li{font-size:15px;color:var(--white);height:33px}
.social{top:4119px;width:48px;height:48px;border-radius:50%;background:var(--gold)}
.rule{left:116px;top:4304px;width:955px;height:1px;background:#6a6a6a}
.copyright{left:0;top:4332px;width:1200px;text-align:center;font-size:16px}
</style>
</head>
<body>

<header class="abs hero" role="img" aria-label="Dark monochrome close-up of a motorcycle engine and chrome wheel"></header>
<nav class="nav">
  <a style="left:99px">Home</a>
  <a style="left:223px">Our Story</a>
  <a style="left:375px">Categories</a>
  <a style="left:765px">Contact</a>
  <a class="small" style="left:948px">Login<svg width="13" height="13" viewBox="0 0 13 13"><circle cx="6.5" cy="4" r="3" fill="#c9a53f"/><path d="M1 13c0-4 2.5-5.5 5.5-5.5S12 9 12 13z" fill="#c9a53f"/></svg></a>
  <a class="small" style="left:1048px">Cart<svg width="15" height="13" viewBox="0 0 15 13"><path d="M0 1h3l2 7h8l2-6H4" stroke="#c9a53f" stroke-width="1.6" fill="none"/><circle cx="6" cy="11" r="1.4" fill="#c9a53f"/><circle cx="12" cy="11" r="1.4" fill="#c9a53f"/></svg></a>
</nav>
<div class="abs brand">Ironvale Locker</div>
<div class="abs hero-kicker">WELCOME TO</div>
<h1 class="abs hero-title">IRONVALE<br>LOCKER</h1>
<p class="abs hero-lead">Lorem ipsum dolor sit amet, consectetur adipiscing elit, sed</p>
<a class="abs btn" style="left:106px;top:431px;width:188px;height:52px">Shop Now</a>
<div class="abs scroll"><span>« Scroll Down</span><i></i></div>

<p class="abs eyebrow" style="top:733px">NEW</p>
<h2 class="abs section-title" style="top:758px">OUR COLLECTIONS</h2>
<article class="abs card" style="left:99px"><div class="photo" role="img" aria-label="Leather bag, belt, watch and wallet on wood" style="background:radial-gradient(ellipse 90px 70px at 210px 270px,#6a4456,rgba(106,68,86,0) 100%),radial-gradient(ellipse 120px 110px at 90px 110px,#8a6a50,rgba(138,106,80,0) 100%),linear-gradient(160deg,#5a3c28,#3a2416 60%,#4a3020)"></div><p>Men's Jewelry</p></article>
<article class="abs card" style="left:440px"><div class="photo" role="img" aria-label="Cigar beside a glass of whiskey on a wooden table" style="background:radial-gradient(ellipse 90px 120px at 215px 220px,#9a5a22,rgba(154,90,34,0) 100%),linear-gradient(180deg,#140c06 0%,#2a1a0c 40%,#6a4220 70%,#3a220e 100%)"></div><p>Cigar &amp; Bar Products</p></article>
<article class="abs card" style="left:779px"><div class="photo" role="img" aria-label="Man in a dark suit holding a cologne bottle" style="background:radial-gradient(ellipse 110px 170px at 190px 230px,#2c3850,rgba(44,56,80,0) 100%),linear-gradient(160deg,#1a1d24,#262c38 55%,#14161c)"></div><p>Man Cave Swag</p></article>

<section class="abs band about"></section>
<div class="abs rider" role="img" aria-label="Black and white photo of a man in a leather jacket seated on a motorcycle"></div>
<p class="abs kicker" style="left:104px;top:1627px">MEN'S PRODUCTS</p>
<h2 class="abs heading" style="left:101px;top:1664px">ABOUT US</h2>
<p class="abs copy" style="left:99px;top:1752px">Sed ut perspiciatis unde omnis iste natus error sit voluptatem<br>accusantium doloremque laudantium, totam rem aperiam, eaque ipsa<br>quae ab illo inventore veritatis et quasi architecto beatae vitae dicta sunt<br>explicabo. Nemo enim ipsam voluptatem quia voluptas sit aspernatur aut<br>odit aut fugit, sed quia consequuntur magni dolores eos qui ratione<br>voluptatem sequi nesciunt. Neque porro quisquam est, qui dolorem ipsum<br>quia dolor sit amet, consectetur, adipisci velit, sed quia non numquam eius<br>modi tempora incidunt ut labore et dolore magnam aliquam quaerat</p>
<p class="abs copy" style="left:99px;top:1985px">Sed ut perspiciatis unde omnis iste natus error sit voluptatem<br>accusantium doloremque laudantium, totam rem aperiam, eaque ipsa<br>quae ab illo inventore veritatis et quasi architecto beatae vitae dicta sunt<br>explicabo. Nemo enim ipsam voluptatem quia voluptatem.</p>
<a class="abs btn" style="left:102px;top:2143px;width:188px;height:52px">Read More</a>

<p class="abs eyebrow" style="top:2485px">NEW</p>
<h2 class="abs section-title" style="top:2526px">MOST POPULAR DESIGNS</h2>
<div class="abs product" style="left:99px"><div class="thumb" role="img" aria-label="Octagonal wooden cigar ashtray" style="background:radial-gradient(ellipse 55px 35px at 65px 75px,#6a2a24 0%,#8a4a40 70%,rgba(220,214,212,0) 100%),#e4e0de"></div></div>
<div class="abs product" style="left:353px"><div class="thumb" role="img" aria-label="Red wooden cigar humidor" style="background:radial-gradient(ellipse 62px 40px at 65px 70px,#7a1414 0%,#9a2a22 75%,rgba(255,255,255,0) 100%),#fff"></div></div>
<div class="abs product" style="left:607px"><div class="thumb" role="img" aria-label="Wooden whiskey decanter set" style="background:radial-gradient(ellipse 45px 55px at 62px 70px,#7a4018 0%,#a86a34 70%,rgba(240,232,222,0) 100%),#f2ebe4"></div></div>
<div class="abs product" style="left:861px"><div class="thumb" role="img" aria-label="Open wooden watch and accessory box" style="background:radial-gradient(ellipse 48px 56px at 65px 68px,#2a1a14 0%,#5a3426 70%,rgba(255,255,255,0) 100%),#fff"></div></div>
<p class="abs pname" style="left:99px">Nemo enim ipsam</p><p class="abs price" style="left:99px">AUD 1,845</p>
<p class="abs pname" style="left:353px">Nemo enim ipsam</p><p class="abs price" style="left:353px">AUD 1,845</p>
<p class="abs pname" style="left:607px">Nemo enim ipsam</p><p class="abs price" style="left:607px">AUD 1,845</p>
<p class="abs pname" style="left:861px">Nemo enim ipsam</p><p class="abs price" style="left:861px">AUD 1,845</p>

<section class="abs band charm"></section>
<div class="abs glass" role="img" aria-label="Glass of whiskey on a dark wooden surface"></div>
<p class="abs kicker" style="left:584px;top:3214px">MEN'S PRODUCTS</p>
<h2 class="abs heading" style="left:581px;top:3250px">AN OLD WORLD CHARM</h2>
<p class="abs copy" style="left:579px;top:3339px">Sed ut perspiciatis unde omnis iste natus error sit voluptatem<br>accusantium doloremque laudantium, totam rem aperiam, eaque ipsa<br>quae ab illo inventore veritatis et quasi architecto beatae vitae dicta sunt<br>explicabo. Nemo enim ipsam voluptatem quia voluptas sit aspernatur aut<br>odit aut fugit, sed quia consequuntur magni dolores eos qui ratione<br>voluptatem sequi nesciunt. Neque porro quisquam est, qui dolorem ipsum<br>quia dolor sit amet, consectetur, adipisci velit, sed quia non numquam eius<br>modi tempora incidunt ut labore et dolore magnam aliquam quaerat</p>
<p class="abs copy" style="left:579px;top:3574px">Sed ut perspiciatis unde omnis iste natus error sit voluptatem<br>accusantium doloremque laudantium, totam rem aperiam, eaque ipsa<br>quae ab illo inventore veritatis et quasi architecto beatae vitae dicta sunt<br>explicabo. Nemo enim ipsam voluptatem quia voluptatem.</p>
<a class="abs btn" style="left:581px;top:3732px;width:188px;height:52px">Shop Now</a>

<footer>
  <div class="abs footer-brand">Ironvale<br>Locker</div>
  <h3 class="abs fhead" style="left:430px">Quick Links</h3>
  <ul class="abs flinks" style="left:433px"><li>Home</li><li>Our Story</li><li style="font-size:17px">Categories</li><li>Contact</li></ul>
  <h3 class="abs fhead" style="left:680px">Help Links</h3>
  <ul class="abs flinks" style="left:683px"><li>Terms &amp; conditions</li><li>Privacy Policy</li><li>About Us</li><li>Support</li></ul>
  <h3 class="abs fhead" style="left:895px">Social Media</h3>
  <span class="abs social" style="left:899px" aria-label="Social profile"></span>
  <span class="abs social" style="left:970px" aria-label="Social profile"></span>
  <div class="abs rule"></div>
  <p class="abs copyright">© 2023&nbsp; Ironvale Locker. All Rights Reserved.</p>
</footer>

</body>
</html>
```